Real Estate Company Looking for Business Card Designs for 3 Executives

Hello!
Thanks so much for considering our project! We are a real estate investment company located in Edmonton, Alberta called Bellcrane Group of Companies. We invest/develop both commercial and residential real estate and are looking to create 3 DOUBLE-SIDED business cards for 3 top executives in the company! (for some reason it won't let us select the double-sided option, but yes, the cards are double sided and would be happy to tip extra)

We have certain guidelines that we want our business cards to for sure follow - the back of the Business card has to be the Black Background Version of the Logo which has already been designed and linked as a file (first file). We want the entire back of the card to simply just be the black background logo. In terms of the front of the card, would like to see a smaller version of the white background logo (linked as the second file) in the top left hand corner - of course, feel free to get creative and we can make revisions together along the way! and Then after that, just text. We want the card to be sharp, clean, easy on the eyes and highly professional looking. We would like the card to include the Full name of the Company (Bellcrane Group of Companies), Name of the Person, Title, Phone, Email. If possible please provide the front part of the card for 3 people:

1) Bellcrane Group of Companies, Nora Lindqvist, Chief Financial Officer, 780-555-0142, noralindqvist@bellcranegroup.example

2) Bellcrane Group of Companies, Julien Lindqvist, Chief Executive Officer, 780-555-0187, julienlindqvist@bellcranegroup.example

3) Bellcrane Group of Companies, Tom Okafor, Chief Operations Officer, 587-555-0163, tomokafor@bellcranegroup.example

Thank you so much for considering our project & we look forward to seeing your designs!

```html
<!DOCTYPE html>
<html lang="en">
<head>
<meta charset="utf-8">
<title>Bellcrane Group of Companies – Business Card</title>
<link href="https://fonts.googleapis.com/css2?family=Montserrat:wght@400;500;700&display=swap" rel="stylesheet">
<style>
  :root {
    --bg: #8a8272;
    --card-white: #f7f7f7;
    --ink: #1b1b1b;
    --ink-soft: #2a2a2a;
    --card-black: #1a1a1a;
    --forest-dark: #222222;
    --forest-mid: #2b2b2b;
    --paper-white: #ffffff;
  }
  * { margin: 0; padding: 0; box-sizing: border-box; }
  html, body {
    width: 1200px; height: 1200px; overflow: hidden;
    background: var(--bg);
    font-family: "Montserrat", Arial, sans-serif;
  }
  .stage { position: relative; width: 1200px; height: 1200px; }

  .card {
    position: absolute; left: 170px; width: 860px; height: 490px;
    border-radius: 22px; overflow: hidden;
  }
  .card--front { top: 90px; background: linear-gradient(160deg, #ffffff 0%, var(--card-white) 100%); color: var(--ink); }
  .card--back  { top: 620px; background: var(--card-black); color: var(--paper-white); }

  /* wordmark */
  .wordmark { position: absolute; text-align: center; font-weight: 500; }
  .wordmark__name { display: block; letter-spacing: 0.42em; }
  .wordmark__sub  { display: block; letter-spacing: 0.2em; }

  .card--front .wordmark { left: 72px; top: 150px; width: 260px; color: var(--ink); }
  .card--front .wordmark__name { font-size: 19px; }
  .card--front .wordmark__sub  { font-size: 11px; margin-top: 12px; }
  .card--front .wordmark__mark {
    width: 44px; height: 44px; background: var(--ink);
    margin: 0 auto 40px;
  }

  .person { position: absolute; right: 70px; top: 130px; text-align: right; }
  .person__name  { font-size: 31px; font-weight: 700; color: var(--ink); }
  .person__title { font-size: 21px; font-weight: 400; color: var(--ink-soft); margin-top: 2px; letter-spacing: 0.02em; }

  .contact { position: absolute; left: 72px; top: 332px; list-style: none; }
  .contact__item {
    display: flex; align-items: center; gap: 16px;
    font-size: 21px; font-weight: 400; letter-spacing: 0.03em;
    height: 36px;
  }
  .contact__icon { width: 22px; height: 22px; flex: none; }

  .accent-block {
    position: absolute; right: 70px; bottom: 0;
    width: 120px; height: 156px; background: var(--card-black);
  }

  /* back */
  .forest {
    position: absolute; left: 0; right: 0; bottom: 0; height: 340px;
    background: linear-gradient(180deg, rgba(40,40,40,0) 0%, var(--forest-mid) 45%, var(--forest-dark) 100%);
  }
  .card--back .wordmark { left: 0; right: 0; top: 150px; color: var(--paper-white); }
  .card--back .wordmark__mark {
    width: 70px; height: 70px; background: var(--paper-white);
    margin: 0 auto 50px;
  }
  .card--back .wordmark__name { font-size: 26px; }
  .card--back .wordmark__sub  { font-size: 16px; margin-top: 16px; }
</style>
</head>
<body>
<div class="stage">

  <section class="card card--front" aria-label="Business card front">
    <div class="wordmark">
      <div class="wordmark__mark"></div>
      <span class="wordmark__name">BELLCRANE</span>
      <span class="wordmark__sub">GROUP OF COMPANIES</span>
    </div>

    <div class="person">
      <p class="person__name">Nora Lindqvist</p>
      <p class="person__title">Chief Financial Officer</p>
    </div>

    <ul class="contact">
      <li class="contact__item">
        <svg class="contact__icon" viewBox="0 0 22 22" aria-hidden="true">
          <circle cx="11" cy="11" r="11" fill="#1b1b1b"/>
          <path d="M7.3 5.8c.5-.4 1.1-.3 1.4.2l1 1.6c.3.5.2 1-.2 1.3l-.7.5c.5 1.2 1.4 2.2 2.6 2.8l.5-.7c.3-.4.9-.5 1.3-.2l1.6 1c.5.3.6.9.2 1.4l-.8.9c-.5.5-1.3.7-2 .4-2.7-1.1-4.7-3.1-5.8-5.8-.3-.7-.1-1.5.4-2z" fill="#fff"/>
        </svg>
        <span>780-555-0142</span>
      </li>
      <li class="contact__item">
        <svg class="contact__icon" viewBox="0 0 22 22" aria-hidden="true">
          <circle cx="11" cy="11" r="11" fill="#1b1b1b"/>
          <rect x="5.5" y="7.5" width="11" height="7.5" rx="0.8" fill="#fff"/>
          <path d="M5.8 8l5.2 4 5.2-4" fill="none" stroke="#1b1b1b" stroke-width="0.9"/>
        </svg>
        <span>noralindqvist@bellcranegroup.example</span>
      </li>
      <li class="contact__item">
        <svg class="contact__icon" viewBox="0 0 22 22" aria-hidden="true">
          <circle cx="11" cy="11" r="11" fill="#1b1b1b"/>
          <g fill="none" stroke="#fff" stroke-width="0.9">
            <circle cx="11" cy="11" r="5.5"/>
            <ellipse cx="11" cy="11" rx="2.4" ry="5.5"/>
            <path d="M5.5 11h11M6.3 8.3h9.4M6.3 13.7h9.4"/>
          </g>
        </svg>
        <span>www.bellcranegroup.example</span>
      </li>
    </ul>

    <div class="accent-block"></div>
  </section>

  <section class="card card--back" aria-label="Business card back">
    <div class="forest" role="img" aria-label="Faint silhouette of a pine forest along the lower part of the card"></div>
    <div class="wordmark">
      <div class="wordmark__mark"></div>
      <span class="wordmark__name">BELLCRANE</span>
      <span class="wordmark__sub">GROUP OF COMPANIES</span>
    </div>
  </section>

</div>
</body>
</html>
```